Baby Shower Invitation for Vectored Image Provided

Caroline & Desmond's Baby Shower - Black/White/Gold Colors preferred
Please use the vectored portrait image attached. I'd like us on the lower right side of the invitation.
Can be horizontal or vertical layout.
The second image attached has the information needed for you to complete.
I don't want that style copied, it is just an example.

```html
<!DOCTYPE html>
<html lang="en">
<head>
<meta charset="UTF-8">
<title>Caroline's Baby Shower Invitation</title>
<link rel="stylesheet" href="https://fonts.googleapis.com/css2?family=Merriweather:wght@900&family=UnifrakturCook:wght@700&family=Josefin+Sans:wght@400&family=Fira+Sans+Condensed:wght@700&family=Lobster+Two:ital,wght@1,700&display=swap">
<style>
  :root {
    --gold: #d8c466;
    --gold-light: #dcc870;
    --gold-text: #cdb64d;
    --black: #000000;
    --white: #ffffff;
    --ink: #1a1a1a;
    --portrait-dark: #2a2a2a;
    --portrait-warm: #b98f6a;
  }
  html, body {
    margin: 0;
    padding: 0;
    overflow: hidden;
    background: var(--white);
  }
  .invitation {
    position: relative;
    width: 857px;
    height: 1200px;
    overflow: hidden;
    background: var(--white);
  }
  .monogram-band {
    position: absolute;
    left: 0; top: 0;
    width: 857px;
    height: 516px;
    background: linear-gradient(180deg, var(--gold-light), var(--gold));
  }
  .monogram {
    position: absolute;
    left: 0; right: 0;
    top: 30px;
    text-align: center;
    font-family: "Merriweather", serif;
    font-weight: 900;
    font-size: 520px;
    line-height: 1;
    color: var(--white);
  }
  .tagline-band {
    position: absolute;
    left: 0; top: 516px;
    width: 857px;
    height: 96px;
    background: var(--black);
    display: flex;
    align-items: center;
    justify-content: center;
  }
  .tagline {
    margin: 0;
    font-family: "UnifrakturCook", serif;
    font-weight: 700;
    font-size: 42px;
    color: var(--white);
    letter-spacing: 0.5px;
  }
  .details {
    position: absolute;
    left: 0;
    width: 480px;
    text-align: center;
    color: var(--ink);
  }
  .line {
    position: absolute;
    left: 0; right: 0;
    margin: 0;
    font-family: "Josefin Sans", sans-serif;
    font-size: 26px;
    line-height: 32px;
    letter-spacing: -0.5px;
  }
  .honoree {
    position: absolute;
    left: 0; right: 0;
    margin: 0;
    font-family: "Fira Sans Condensed", sans-serif;
    font-weight: 700;
    font-size: 38px;
    line-height: 44px;
    letter-spacing: 1.5px;
    color: var(--gold-text);
  }
  .divider {
    position: absolute;
    left: 180px;
    top: 995px;
  }
  .registry {
    position: absolute;
    left: 0; right: 0;
    margin: 0;
    font-family: "Lobster Two", sans-serif;
    font-style: italic;
    font-weight: 700;
    font-size: 26px;
    line-height: 32px;
    color: var(--gold-text);
  }
  .portrait {
    position: absolute;
    left: 472px;
    top: 644px;
    width: 385px;
    height: 556px;
    background: linear-gradient(160deg, var(--portrait-warm) 0%, var(--portrait-dark) 55%, var(--black) 100%);
    border-radius: 120px 120px 0 0;
  }
</style>
</head>
<body>
<main class="invitation">
  <section class="monogram-band">
    <div class="monogram">C</div>
  </section>

  <section class="tagline-band">
    <h1 class="tagline">A little man is on the way</h1>
  </section>

  <section class="details">
    <p class="line" style="top:644px;">Please join us for a</p>
    <p class="line" style="top:677px;">Baby Shower honoring:</p>
    <h2 class="honoree" style="top:732px;">CAROLINE HOLLOWELL</h2>
    <p class="line" style="top:800px;">Sunday, September 1<sup style="font-size:12px;">st</sup></p>
    <p class="line" style="top:834px;">11:30am-2:30pm</p>
    <p class="line" style="top:881px;">The Maplewood</p>
    <p class="line" style="top:916px;">1480 Birchway Ave</p>
    <p class="line" style="top:950px;">Raleigh, NC</p>
    <svg class="divider" width="140" height="14" viewBox="0 0 140 14" aria-hidden="true">
      <g fill="var(--gold-text)">
        <circle cx="7" cy="7" r="6.5"/><circle cx="22.75" cy="7" r="6.5"/><circle cx="38.5" cy="7" r="6.5"/>
        <circle cx="54.25" cy="7" r="6.5"/><circle cx="70" cy="7" r="6.5"/><circle cx="85.75" cy="7" r="6.5"/>
        <circle cx="101.5" cy="7" r="6.5"/><circle cx="117.25" cy="7" r="6.5"/><circle cx="133" cy="7" r="6.5"/>
      </g>
    </svg>
    <p class="line" style="top:1033px;">RSVP to Desmond:</p>
    <p class="line" style="top:1065px;">919-555-0148</p>
    <p class="line" style="top:1096px;">by August 20th</p>
    <p class="registry" style="top:1151px;">Caroline is registered at Little Nest Baby</p>
  </section>

  <div class="portrait" role="img" aria-label="Illustrated portrait of the expecting couple, standing together with hands on the baby bump"></div>
</main>
</body>
</html>
```